Trifold Brochure Design Project

We need a trifold brochure design for a company/product called VitaLens. We provide full-body MRI screening, along with blood chemistry and DNA analysis, followed by a consultation with the MD in a comfortable outpatient setting.
The facility is located in Fort Lauderdale, Florida.
The concept is that people usually don't know about many diseases until they are far advanced and more difficult to treat. We offer early detection which leads to early treatment and better outcomes.
The concept should blend an emotional construct (do it for yourself or someone you love, the best gift is health, live longer to love longer, etc) with science to legitimize the service. (MRI, Blood Chemistry, DNA analysis and an MD to interpret)

Target Market(s)

Baby boomers and active middle-age men and women

Industry/Entity Type

It Company

Requirements
Must have
• Attractive middle age people enjoying life because they know they are healthy.
Services are provided 7-days a week in a comfortable outpatient setting. Everything is totally confidential.
VitaLens is a division of Corlane Diagnostic & Imaging Centers
Nice to have
• Some clinical imagery such as the doctor, the MRI machine or inferences that this is a clinical-based solution.
Extremely experienced, qualified and licensed Doctors and Technologists are involved.

```html
<!DOCTYPE html>
<html lang="en">
<head>
<meta charset="utf-8">
<title>VitaLens Trifold Brochure</title>
<link href="https://fonts.googleapis.com/css2?family=Open+Sans:wght@400;600&family=Roboto+Condensed:wght@400;700&family=Arimo&display=swap" rel="stylesheet">
<style>
  :root {
    --teal: #74d5c6;
    --blue: #1b63b5;
    --ink-blue: #2340a0;
    --ink-navy: #1a2c86;
    --white: #ffffff;
  }
  * { margin: 0; padding: 0; box-sizing: border-box; }
  html, body { width: 1200px; height: 900px; overflow: hidden; background: var(--white); }
  .brochure { position: relative; width: 1200px; height: 900px; background: var(--white); font-family: "Open Sans", Arial, sans-serif; }
  .shapes { position: absolute; inset: 0; }
  .panel-heading {
    position: absolute; color: var(--white); font-family: "Open Sans", Arial, sans-serif;
    font-weight: 400; font-size: 21px; letter-spacing: 0.1px; white-space: nowrap;
  }
  .body-copy {
    position: absolute; color: var(--white); font-size: 12px; line-height: 17.6px;
    letter-spacing: -0.15px; text-align: justify; text-indent: 52px;
  }
  .body-copy.dark { color: var(--ink-navy); }
  .photo { position: absolute; }
  .detect-list {
    position: absolute; font-family: "Roboto Condensed", "Arial Narrow", sans-serif;
    color: var(--ink-blue); font-size: 17px; line-height: 22.2px; list-style: none;
    white-space: nowrap;
  }
  .detect-list .group-title { font-weight: 700; }
  .detect-list .more { font-weight: 700; }
  .tagline {
    position: absolute; left: 800px; width: 400px; top: 522px; text-align: center;
    font-family: "Arimo", Arial, sans-serif; color: var(--teal); font-size: 26px; line-height: 28px;
  }
</style>
</head>
<body>
<main class="brochure">
  <svg class="shapes" width="1200" height="900" viewBox="0 0 1200 900" aria-hidden="true">
    <defs>
      <linearGradient id="blueBand" x1="0" y1="0" x2="1" y2="1">
        <stop offset="0" stop-color="#1560b0"/>
        <stop offset="0.6" stop-color="#2a78c6"/>
        <stop offset="1" stop-color="#0d3f88"/>
      </linearGradient>
      <linearGradient id="blueCorner" x1="0" y1="0" x2="1" y2="0">
        <stop offset="0" stop-color="#2a78c6"/>
        <stop offset="1" stop-color="#0d3f88"/>
      </linearGradient>
    </defs>
    <rect x="0" y="28" width="1200" height="72" fill="var(--teal)"/>
    <polygon points="0,28 330,28 400,100 0,100" fill="url(#blueBand)"/>
    <polygon points="725,28 800,28 800,100" fill="url(#blueCorner)"/>
    <polygon points="800,28 1130,28 1200,100 800,100" fill="var(--blue)"/>
    <polygon points="1130,28 1200,28 1200,100" fill="var(--teal)"/>
    <rect x="0" y="100" width="400" height="208" fill="var(--teal)"/>
    <polygon points="0,325 330,325 400,400 0,400" fill="url(#blueBand)"/>
    <polygon points="400,552 730,552 800,630 400,630" fill="url(#blueBand)"/>
    <polygon points="730,552 800,552 800,630" fill="var(--teal)" opacity="0.9"/>
    <rect x="400" y="630" width="400" height="244" fill="var(--teal)"/>
    <rect x="800" y="100" width="400" height="410" fill="var(--teal)"/>
  </svg>

  <h2 class="panel-heading" style="left:38px; top:60px;">Why MRI?</h2>
  <p class="body-copy" style="left:38px; top:115px; width:324px;">The MRI Scan is considered the Gold Standard for soft-tissue analysis. MRI uses a strong magnetic field and radio waves to generate extremely accurate images of the inside of your body. Traditionally MRI has been used to answer specific questions when patients are symptomatic. Unfortunately many diseases do not produce symptoms until they are well advanced. Recent advances in MRI technology have allowed us to offer screening MRI to the public, without a prescription. This is a revolutionary application for MRI, giving hope for early detection to millions.</p>

  <h2 class="panel-heading" style="left:38px; top:363px;">Expert Clinicians</h2>
  <div class="photo" role="img" aria-label="Portrait of the medical director in a white shirt and tie, smiling"
       style="left:0; top:400px; width:400px; height:226px; background:linear-gradient(135deg,#f4f4f4 0%,#e9e4e1 45%,#d9c2b6 60%,#eceff2 100%);"></div>
  <div style="position:absolute; left:0; top:626px; width:400px; height:248px; background:linear-gradient(180deg,#f3f4f8,#ffffff);"></div>
  <p class="body-copy dark" style="left:38px; top:652px; width:324px;">Dr. Martin Hale is a pioneer and leading expert in the field of MRI, as well as preventative diagnostics. Since 1983, when he brought the first MRI machine to Florida, Dr. Hale has worked on the cutting edge of diagnostic imaging science, perfecting the balance between predictive and preventative medicine. The VitaLensTM technical staff is the most experienced and professional anywhere, with average experience levels of 20+ years, and advanced diagnostic imaging degrees. Excellence in customer service is our primary focus, and our goal is keeping our clients healthy.</p>

  <h2 class="panel-heading" style="left:438px; top:60px;">What MRI can detect?</h2>
  <ul class="detect-list" style="left:438px; top:116px;">
    <li class="group-title">Organs:</li>
    <li>• Brain</li><li>• Face</li><li>• Neck</li><li>• Thyroid</li><li>• Lungs</li><li>• Heart</li><li>• Breasts</li>
    <li>&nbsp;</li>
    <li class="group-title">Diseases:</li>
    <li>• Cancer</li><li>• Heart Disease</li><li>• Fracture</li><li>• Cyst</li><li>• Lipoma</li><li>• Abscess</li><li>• Plaque</li><li>• Aneurysm</li><li>• Tissue breakdown</li>
  </ul>
  <ul class="detect-list" style="left:610px; top:138.2px;">
    <li>• Spine</li><li>• Liver</li><li>• Kidneys</li><li>• Spleen</li><li>• Pancreas</li><li>• Prostate</li><li>• Uterus/Ovaries</li><li>• Bladder</li>
    <li>&nbsp;</li>
    <li>• MS</li><li>• Osteomyelitis</li><li>• Pulmonary embo-</li><li>lism</li><li>• Emphysema</li><li>• Arthritis</li><li>• Osteoporosis</li>
    <li>&nbsp;</li>
    <li class="more">...and many more</li>
  </ul>

  <h2 class="panel-heading" style="left:438px; top:591px;">Take Control of Your Health</h2>
  <p class="body-copy" style="left:438px; top:652px; width:324px;">Love Life? We’ll help you stick around to enjoy more of it. VitaLens is the high resolution, full body health analysis exclusively from Corlane Diagnostic &amp; Imaging Centers. Now you can be proactive about your health. In about an hour, we will provide you with the most complete objective analysis of the actual state of your health available anywhere. Full Body MRI, Blood Chemistry and DNA Analysis followed by a consultation with the doctor. Take Control! Give VitaLens a call today. We have plans for every budget and need. Do it for yourself, or do it for someone you love but do it today.</p>

  <h2 class="panel-heading" style="left:838px; top:62px;">The Complete Package</h2>
  <p class="body-copy" style="left:838px; top:118px; width:324px;">In addition to scanning your body using high-resolution MRI, we also perform blood and DNA analysis to determine if you have the potential for disease, or very early proto-disease that is not yet observable. By analyzing the hundreds of MRI images, the blood chemistry and DNA analysis, our clinicians can provide you with a comprehensive “road map” of health for your entire body now, and into the future. We also offer individual exams on specific organ systems, extremities, gender-specific exams and specific pathology search. Once the analysis is complete, each VitaLensTM patient has the opportunity to sit with Dr. Hale one-on-one for a 30-minute consultation. This consultation is invaluable and includes not only a complete review of your anatomy, physiology and any pathology found, but recommendations for a wide array of corrective actions from minor to major. Once complete, you are provided with a written report and DVD containing all the information and images acquired about your own body. Taking control of your health is now in your hands. Knowledge is the key, and Dr. Hale can give you the knowledge you need.</p>

  <p class="tagline">The safest and most complete<br>body scan available.</p>
  <div class="photo" role="img" aria-label="Smiling middle-aged couple in white robes embracing"
       style="left:800px; top:590px; width:400px; height:284px; background:linear-gradient(120deg,#e8e6e2 0%,#c99a7e 40%,#d7b08f 60%,#f1ede8 100%);"></div>
</main>
</body>
</html>
```